Website Redesign for Accommodation Directory

We need a redesign for stayfinderhubzone.example
The new design needs to include a banner with overlaid text and a 'get started now' button. The overlaid text could be 'Find Hotels in Auckland, New Zealand' for example.
The new design needs to include:
- primary navigation in header
- an accommodation search (left or right column)
- a secondary navigation menu (under the search).
We will need the following font styles (including links for each) defined also please:
h1, h2, h3, h4, h5, h6, p, ul, ol, address, pre
Accommodation

```html
<!DOCTYPE html>
<html lang="en">
<head>
<meta charset="utf-8">
<title>Stay Finder Hub Zone</title>
<link href="https://fonts.googleapis.com/css2?family=Open+Sans:wght@400;600&family=Arimo:wght@400;700&display=swap" rel="stylesheet">
<style>
  :root {
    --backdrop: #2f7f96;
    --page-dark: #333333;
    --header-bg: #ececec;
    --content-bg: #f3f3f3;
    --nav-red-top: #d93440;
    --nav-red-bottom: #b11d28;
    --brand-grey: #4a4a4a;
    --cta-top: #f7892a;
    --cta-bottom: #f0541f;
    --menu-brown: #6e5d52;
    --menu-grey-a: #bdbdbd;
    --menu-grey-b: #f2f2f2;
    --text: #111111;
    --white: #ffffff;
  }
  * { box-sizing: border-box; margin: 0; padding: 0; }
  html, body { width: 1200px; height: 869px; overflow: hidden; }
  body {
    position: relative;
    font-family: "Arimo", Arial, sans-serif;
    background: var(--backdrop);
  }
  .backdrop-pattern {
    position: absolute; inset: 0;
    background: linear-gradient(135deg, #3a8ea5, #26718a);
  }
  .page {
    position: absolute; left: 100px; top: 18px; width: 1018px; height: 828px;
    background: var(--page-dark);
    box-shadow: 0 0 10px rgba(0,0,0,.45);
  }
  .site-header {
    position: absolute; left: 0; top: 12px; width: 100%; height: 126px;
    background: linear-gradient(#f1f1f1, #e6e6e6);
  }
  .brand-name {
    position: absolute; left: 25px; top: 42px;
    font-family: "Arimo", Arial, sans-serif; font-weight: 400;
    font-size: 34px; line-height: 40px; color: var(--brand-grey);
  }
  .primary-nav {
    position: absolute; left: 503px; top: 44px; width: 494px; height: 38px;
    border-radius: 12px; border: 1px solid #9a9a9a;
    background: linear-gradient(var(--nav-red-top), var(--nav-red-bottom));
    display: flex; align-items: center; justify-content: space-around; padding: 0 20px 0 30px;
  }
  .primary-nav a { color: var(--white); text-decoration: none; font-size: 17px; }
  .banner {
    position: absolute; left: 0; top: 147px; width: 100%; height: 266px;
  }
  .banner-photo {
    position: absolute; inset: 0;
    background: linear-gradient(90deg, #6b4a2c 0%, #3b3533 30%, #353535 55%, #4a3a30 72%, #8a6a48 100%);
  }
  .banner-title {
    position: absolute; left: 0; width: 1102px; top: 12px; text-align: center;
    font-family: "Open Sans", sans-serif; font-weight: 400; font-size: 29px; line-height: 40px;
    color: var(--white); letter-spacing: 1px;
  }
  .search-panel {
    position: absolute; left: 44px; top: 72px; width: 234px; height: 186px;
    border: 1px solid #cfcfcf; border-radius: 10px;
    background: rgba(90,80,75,.75);
    padding: 20px 16px 0 16px;
  }
  .search-panel h2 {
    font-weight: 400; font-size: 13.5px; line-height: 16px; color: var(--white);
    letter-spacing: 0.3px; white-space: nowrap; margin-bottom: 22px;
  }
  .select {
    position: relative; height: 25px; background: var(--white); border: 1px solid #999;
    font-size: 13px; color: #333; padding: 5px 9px; margin-bottom: 11px; letter-spacing: 0.3px;
  }
  .select-arrow {
    position: absolute; right: 0; top: 0; width: 33px; height: 23px; border-left: 1px solid #999;
    background: linear-gradient(#fafafa, #ddd);
  }
  .select-arrow svg { position: absolute; left: 9px; top: 6px; }
  .go-button {
    position: absolute; right: 17px; top: 135px; width: 64px; height: 24px;
    background: #5d534e; border: 1px solid #c8c8c8; color: var(--white);
    font-size: 14px; text-align: center; line-height: 22px;
  }
  .cta {
    position: absolute; left: 432px; top: 114px; width: 202px; height: 66px;
    border-radius: 10px; border: 1px solid #f6d3b5;
    background: linear-gradient(var(--cta-top), var(--cta-bottom) 50%);
    color: var(--white); font-family: "Open Sans", sans-serif; font-weight: 600; font-size: 19px;
    text-align: center; line-height: 64px; letter-spacing: 0.3px;
  }
  .content {
    position: absolute; left: 0; top: 423px; width: 100%; height: 353px; background: var(--content-bg);
  }
  .submenu-frame {
    position: absolute; left: 42px; top: 11px; width: 234px; height: 325px;
    border: 1px solid #a8a8a8; border-radius: 10px;
  }
  .submenu {
    position: absolute; left: 15px; top: 12px; width: 204px; height: 300px;
    background: var(--page-dark); border-radius: 10px; list-style: none; padding: 9px 0 0 14px;
  }
  .submenu li {
    width: 177px; height: 41px; margin-bottom: 7px; border-radius: 6px; overflow: hidden;
    background: radial-gradient(ellipse 52px 80px at 0% 50%, var(--menu-brown) 99%, transparent 100%),
                linear-gradient(90deg, var(--menu-grey-a), var(--menu-grey-b));
    color: var(--white); font-size: 15px; line-height: 41px; padding-left: 27px; letter-spacing: 0.3px;
  }
  .intro {
    position: absolute; left: 322px; top: 55px; font-size: 21px; line-height: 25.5px;
    letter-spacing: 0.6px; color: var(--text); white-space: nowrap;
  }
  .site-footer {
    position: absolute; left: 0; bottom: 0; width: 100%; height: 52px;
    color: var(--white); font-size: 17px; text-align: right; padding: 17px 27px 0 0; letter-spacing: 0.3px;
  }
</style>
</head>
<body>
  <div class="backdrop-pattern" role="img" aria-label="Teal background with a decorative floral scroll pattern"></div>
  <div class="page">
    <header class="site-header">
      <div class="brand-name">Stay Finder Hub Zone</div>
      <nav class="primary-nav">
        <a href="#">Home</a>
        <a href="#">Add Your Property</a>
        <a href="#">Supplier Login</a>
      </nav>
    </header>

    <section class="banner">
      <div class="banner-photo" role="img" aria-label="Photo of warmly lit resort bedrooms with a bed and orange cushions"></div>
      <h1 class="banner-title">Find Accommodation in Any Country</h1>
      <form class="search-panel">
        <h2>ACCOMMODATION SEARCH</h2>
        <div class="select">All Countries
          <span class="select-arrow"><svg width="14" height="10"><path d="M0 0h14L7 10z" fill="#555"/></svg></span>
        </div>
        <div class="select">All Categories
          <span class="select-arrow"><svg width="14" height="10"><path d="M0 0h14L7 10z" fill="#555"/></svg></span>
        </div>
        <div class="go-button">Go</div>
      </form>
      <a class="cta">GET STARTED NOW</a>
    </section>

    <main class="content">
      <div class="submenu-frame">
        <ul class="submenu">
          <li>Submenu1</li>
          <li>Submenu2</li>
          <li>Submenu3</li>
          <li>Submenu4</li>
          <li>Submenu5</li>
          <li>Submenu6</li>
        </ul>
      </div>
      <p class="intro">
        Lorem ipsum dolor sit amet, consectetur adipiscing elit.<br>
        Sed porttitor ligula ornare lectus consequat mattis.<br>
        Sed sed lorem in nisl molestie iaculis.<br>
        Donec in felis eget orci mattis tincidunt eget vel orci.<br>
        Sed sed sem ligula. Phasellus iaculis pretium magna,<br>
        vitae mattis mauris interdum elementum.<br>
        Etiam lacinia condimentum arcu at pellentesque.<br>
        Donec adipiscing cursus velit, et tempor libero scelerisque sed.
      </p>
    </main>

    <footer class="site-footer">© 2011 Stay Finder Hub Zone</footer>
  </div>
</body>
</html>
```